Pharmacy Moving Flyer Design

We are a community pharmacy that is relocating to new premises and as a result changing our name also. Our current name is Mill Lane Pharmacy and our new name will be Bramble Yard Pharmacy. I want to include a relocation map and also stress the fact that the only thing changing is the name and the location. Everything else will stay the same but newer!
Current address is 41 Foxwell Road, Oswestry, TQ47 9LM. New address Bramble Yard Pharmacy, 62 Harrowby Close, Oswestry, TQ47 3KD. The phone numbers will remain the same - 01784 390517 and 0800 4837206. The date for opening in our new location is Monday 17th November 2014.

```html
<!DOCTYPE html>
<html lang="en">
<head>
<meta charset="utf-8">
<title>Mill Lane Pharmacy is Moving – Bramble Yard Pharmacy</title>
<link rel="stylesheet" href="https://fonts.googleapis.com/css2?family=Cinzel:wght@400;700&family=Open+Sans:ital,wght@0,400;0,700;1,700&family=PT+Sans+Narrow:wght@400&display=swap">
<style>
  :root {
    --navy: #233f8c;
    --red: #e3283a;
    --bar-red: #d9534f;
    --grey: #8e8b8a;
    --white: #ffffff;
    --ink: #1d1d1d;
    --page: #e9e9e9;
    --map-text: #8d98c7;
    --photo-light: #fbfbfb;
    --photo-mid: #ececec;
    --ribbon-deep: #b81a28;
    --ribbon-soft: #f4e3e4;
  }
  * { margin: 0; padding: 0; box-sizing: border-box; }
  html, body { width: 1200px; height: 969px; overflow: hidden; background: var(--page); }
  .flyer {
    position: absolute; left: 40px; top: 88px;
    width: 918px; height: 650px;
    transform: scale(1.22); transform-origin: 0 0;
    background: var(--white); overflow: hidden;
    font-family: "Open Sans", sans-serif;
  }
  .pills-photo {
    position: absolute; left: 0; top: 0; width: 918px; height: 650px;
    background: linear-gradient(180deg, var(--photo-light) 0%, var(--photo-light) 40%, var(--photo-mid) 100%);
  }
  .ribbon-photo {
    position: absolute; left: 700px; top: 0; width: 218px; height: 305px;
    background: linear-gradient(215deg, var(--ribbon-deep) 0%, var(--red) 40%, var(--ribbon-soft) 85%, var(--photo-light) 100%);
  }
  .shapes { position: absolute; left: 0; top: 0; }
  .tagline {
    position: absolute; left: 0; top: 0; width: 470px; height: 110px;
    display: flex; align-items: center; justify-content: center; flex-direction: column;
    color: var(--white); font-family: "PT Sans Narrow", sans-serif; font-size: 23px; line-height: 1.35; text-align: center;
  }
  .current {
    position: absolute; left: 0; top: 150px; width: 272px; text-align: center; color: var(--white);
    font-family: "PT Sans Narrow", sans-serif;
  }
  .current .label { font-family: "Open Sans", sans-serif; font-size: 20px; }
  .current .name { font-size: 36px; margin-top: 14px; line-height: 1.1; }
  .current .kind { font-size: 23px; letter-spacing: 9px; margin-top: 2px; }
  .current .address { font-size: 23px; line-height: 1.5; margin-top: 20px; }
  .opening { position: absolute; left: 450px; top: 45px; width: 300px; text-align: center; color: var(--ink); }
  .opening .title { color: var(--red); font-weight: 700; font-style: italic; font-size: 34px; line-height: 1.1; letter-spacing: .5px; }
  .opening .date { font-size: 17px; line-height: 1.5; margin-top: 4px; }
  .new-name { position: absolute; left: 380px; top: 183px; width: 430px; text-align: center; color: var(--navy); }
  .new-name .label { font-size: 25px; }
  .new-name .name { font-family: "Cinzel", serif; font-weight: 700; font-size: 44px; line-height: 1.15; margin-top: 8px; white-space: nowrap; }
  .new-name .kind { font-family: "Cinzel", serif; font-size: 31px; letter-spacing: 10px; padding-left: 10px; }
  .circle {
    position: absolute; top: 350px; width: 180px; height: 180px; border-radius: 50%;
    background: var(--navy); display: flex; align-items: center; justify-content: center; text-align: center;
  }
  .circle.address { left: 423px; color: var(--white); font-size: 18px; line-height: 1.4; padding: 0 12px; }
  .circle.map { left: 602px; color: var(--map-text); font-size: 22px; }
  .call-bar {
    position: absolute; left: 45px; top: 558px; width: 828px; height: 58px;
    background: var(--bar-red); border-radius: 3px; display: flex; align-items: center; justify-content: center;
    color: var(--white); font-weight: 700; font-size: 21.5px; white-space: nowrap;
  }
</style>
</head>
<body>
<main class="flyer">
  <div class="pills-photo" role="img" aria-label="Photo of red and white capsules and white tablets"></div>
  <div class="ribbon-photo" role="img" aria-label="Photo of gold scissors cutting a red ribbon"></div>

  <svg class="shapes" width="918" height="650" viewBox="0 0 918 650" aria-hidden="true">
    <polygon points="0,0 425,0 485,55 425,110 0,110" fill="var(--navy)"/>
    <polygon points="0,110 288,110 240,488 0,462" fill="var(--grey)"/>
    <polygon points="288,110 294,110 253,537 240,488" fill="var(--red)"/>
    <polygon points="0,462 253,537 0,474" fill="var(--red)"/>
  </svg>

  <div class="tagline">
    <p>Only thing changing is the name and the location.</p>
    <p>Everything else will stay the same but newer!</p>
  </div>

  <section class="current">
    <p class="label">Current Name</p>
    <p class="name">MILL LANE</p>
    <p class="kind">PHARMACY</p>
    <p class="address">41 FOXWELL ROAD,<br>OSWESTRY,<br>TQ47 9LM</p>
  </section>

  <section class="opening">
    <p class="title">OPENING</p>
    <p class="date">Monday 17th<br>November 2014.</p>
  </section>

  <section class="new-name">
    <p class="label">New Name</p>
    <p class="name">BRAMBLE YARD</p>
    <p class="kind">PHARMACY</p>
  </section>

  <div class="circle address">62 Harrowby Close, Oswestry, TQ47 3KD</div>
  <div class="circle map">Map</div>

  <div class="call-bar">For more information Call Us on 01784 390517 and 0800 4837206</div>
</main>
</body>
</html>
```